The Fern Lantern Pub- restaurant menu, new launch

This is a new restaurant launching Summer 2017. Restaurant is a conversion of long standing small town existing family pizza/italian restaurant. new concept shifts concept to a family pub atmosphere featuring familiar appetizers, burgers, wood-fired pizza, and daily specials, draft beer, full- bar.

atmosphere is casual. want menu to reflect a more current "vibe" than the old place did. Not cold and modern, but retain the cozy familiar feel, without seeming dated and old fashioned.

4 panel menu; 8.5 X 11; 2-4 color
Updates

Project Deadline Extended
Reason: I am interested in seeing more designs. I will be providing feedback in the next few days on all designs submitted. I will also be increasing the budget.

Target Market(s)

Family-Oriented Pub, rural location Berkshire County, MA. Mostly Blue collar customer, value oriented

Industry/Entity Type

American Restaurant

Font styles to use
Sans Serif

Colors

Designer to choose colors to be used in the design.

Requirements
Must have
• Clear, uncluttered design, Highlighted items as specified in draft file (to come)
• ability to make changes daily as menu changes
• each panel separate sheet to slide into binder sleeve

```html
<!DOCTYPE html>
<html lang="en">
<head>
<meta charset="utf-8">
<title>Wood Fired Pizza – The Fern Lantern Pub</title>
<link rel="stylesheet" href="https://fonts.googleapis.com/css2?family=Montserrat:wght@300;400;600;700;800&display=swap">
<style>
  :root {
    --page-bg: #f2f2f2;
    --sheet: #ffffff;
    --charcoal: #3b3b3d;
    --ink: #1e1e1e;
    --heading-grey: #58585a;
    --orange: #ee6a2b;
    --accent-red: #b6434f;
    --photo-dark: #2b3146;
    --photo-warm: #d69a55;
  }
  * { box-sizing: border-box; margin: 0; padding: 0; }
  html, body { width: 1200px; height: 1200px; overflow: hidden; background: var(--page-bg); }
  body { font-family: "Montserrat", sans-serif; color: var(--ink); position: relative; }

  .menu-sheet {
    position: absolute; left: 141px; top: 0;
    width: 1101px; height: 1441px;
    transform: scale(0.8327); transform-origin: top left;
    background: var(--sheet);
    overflow: hidden;
  }
  .header-band { position: absolute; left: 0; top: 0; width: 100%; height: 243px; background: var(--charcoal); }

  .title-box {
    position: absolute; left: 466px; top: 40px; width: 630px; height: 159px;
    background: var(--sheet); text-align: center;
  }
  .title-box .title-top { display: block; font-weight: 300; font-size: 62px; line-height: 1; margin-top: 12px; letter-spacing: 1px; }
  .title-box .title-main { display: block; font-weight: 800; font-size: 84px; line-height: 1; color: var(--orange); letter-spacing: 40px; margin-left: 40px; margin-top: 2px; }

  .hero-photo { position: absolute; left: 20px; top: 14px; width: 420px; height: 420px; }

  .divider { position: absolute; height: 4px; background: var(--accent-red); }
  .divider--top { left: 440px; top: 268px; width: 648px; }
  .divider--left { left: 30px; width: 374px; }

  .rule { position: absolute; left: 416px; width: 641px; height: 2px; background: var(--accent-red); }

  .intro-box {
    position: absolute; left: 452px; top: 299px; width: 623px; height: 141px;
    border: 2px solid var(--accent-red);
    font-size: 21px; line-height: 27px; text-align: center; padding-top: 13px;
  }

  .section-label { position: absolute; left: 40px; width: 365px; height: 70px; }
  .section-label .brace { position: absolute; top: 0; font-weight: 300; font-size: 66px; line-height: 62px; color: var(--accent-red); transform: scaleX(0.7); }
  .section-label .brace--open { left: 0; }
  .section-label .brace--close { right: 0; }
  .section-label h2 { text-align: center; font-size: 25px; font-weight: 700; color: var(--heading-grey); line-height: 62px; }

  .price { position: absolute; left: 40px; width: 355px; text-align: center; font-size: 21px; }

  .copy { position: absolute; left: 454px; width: 640px; font-size: 21px; line-height: 27px; white-space: nowrap; }
  .copy p + p { margin-top: 20px; }
</style>
</head>
<body>
<main class="menu-sheet">
  <div class="header-band"></div>

  <svg class="hero-photo" viewBox="0 0 420 420" role="img" aria-label="Photo of wood fired pizzas topped with zucchini and red pepper">
    <circle cx="210" cy="210" r="206" fill="none" stroke="#ffffff" stroke-width="1.5"/>
    <circle cx="210" cy="210" r="192" fill="none" stroke="#ffffff" stroke-width="3"/>
    <defs>
      <radialGradient id="pizzaTones" cx="50%" cy="48%" r="55%">
        <stop offset="0%" stop-color="#c9803f"/>
        <stop offset="45%" stop-color="#d69a55"/>
        <stop offset="75%" stop-color="#6a5a52"/>
        <stop offset="100%" stop-color="#2b3146"/>
      </radialGradient>
    </defs>
    <circle cx="210" cy="210" r="178" fill="url(#pizzaTones)"/>
  </svg>

  <header class="title-box">
    <h1><span class="title-top">WOOD FIRED</span><span class="title-main">PIZZA</span></h1>
  </header>

  <div class="divider divider--top"></div>

  <div class="intro-box">
    All our dough is made fresh daily in house with just<br>
    four ingredients- water flour salt and yeast.<br>
    Baked to perfection in the wood over, Fern Lantern<br>
    Pizza is the best in the county!
  </div>

  <!-- Specialty pies -->
  <div class="section-label" style="top:527px"><span class="brace brace--open">{</span><h2>Our Specialty Pies</h2><span class="brace brace--close">}</span></div>
  <div class="price" style="top:633px">Small $13</div>
  <div class="price" style="top:698px">Large $17</div>
  <div class="copy" style="top:470px">
    <p>The Buffalo Bird- buffalo sauce, grilled chicken,<br>mozzarella and topped with red onion for just the<br>right finish.&nbsp; Don’t like onion?&nbsp; We’ll leave it off!</p>
    <p>Chicken ‘Q- house made BBQ sauce from Bo Reed’s<br>BBQ, Grilled chicken and mozzarella make this<br>crowd favorite.</p>
    <p>The Hula Hula- Sliced ham and Pineapple, and<br>mozzarella.&nbsp; It doesn’t get any better!&nbsp; Ask for<br>coconut, if you’re feeling crazy!</p>
  </div>

  <div class="divider divider--left" style="top:770px"></div>
  <div class="rule" style="top:767px"></div>

  <!-- Create your own -->
  <div class="section-label" style="top:848px"><span class="brace brace--open">{</span><h2>Create Your Own</h2><span class="brace brace--close">}</span></div>
  <div class="price" style="top:947px">Small $11</div>
  <div class="price" style="top:1012px">Large $15</div>
  <div class="copy" style="top:793px;left:456px">
    <p>Choose from standard toppings for $2.00:</p>
    <p style="margin-top:27px">Pepperoni, Onion, Tomato, Garlic, Green Pepper,<br>Mushroom, Sliced or Chopped Tomato, Broccoli,<br>Spinach, Sliced black olives</p>
    <p style="margin-top:28px">More Meats $2.50:<br>Meatball, Bacon, Sausage, Chicken, Ham</p>
    <p style="margin-top:31px">Specialty Toppings $3.00:</p>
    <p style="margin-top:27px">Xtra Cheese, Pineapple, Feta, Ricotta, Kalamata<br>Olives, Hot Peppers, Coconut, Artichokes, Sun dried<br>Tomato, Pesto</p>
  </div>

  <div class="divider divider--left" style="top:1198px"></div>
  <div class="rule" style="top:1196px"></div>

  <!-- Gluten free -->
  <div class="section-label" style="top:1222px"><span class="brace brace--open">{</span><h2>Gluten Free</h2><span class="brace brace--close">}</span></div>
  <div class="copy" style="top:1242px">Available in Small size only- add $2.00</div>

  <div class="divider divider--left" style="top:1314px"></div>
  <div class="rule" style="top:1311px"></div>

  <!-- Calzone -->
  <div class="section-label" style="top:1333px"><span class="brace brace--open">{</span><h2>Fold It Up!</h2><span class="brace brace--close">}</span></div>
  <div class="copy" style="top:1335px">Turn your Pizza into a calzone, specialty or build your<br>own.&nbsp; Same price as a small.</div>
</main>
</body>
</html>
```